One of Australia's fastest growing Financial Company looking for an updated business card design!

Meridale Holdings Australia is looking for an updated design for our business cards. We would like to keep up our professional appearances and have get new exciting design that fits our company.

The Meridale aim is to facilitate and assist clients in every financial requirement that may arise in financial areas.

We would to see the design to use colour blue and we like the clouds in the background. We have attached two designs we have use before but we need something with more professional and easy to read design.

We would like the website in the back of the card; the employees name more central and stands out; only a postal address; a list of all our locations along the bottom (Sydney, Melbourne, Brisbane, Singapore)

Looking forward to seeing the designs come in!

Target Market(s)

Other Industry Professionals
Middle Class Families

Industry/Entity Type

Finance

Contact Information for Business Card

Name; Company Role; Office Number; Mobile Number; Email Address; Website; Postal Address; Locations

Font styles to use
Serif
Sans Serif

Colors
0492cd
33a6d7
85cae6
85acd3
3176b5
0455a3
cee9f5
d5e2ee

Requirements
Must have
• Name; Company Role; Office Number; Mobile Number; Email Address; Website; Postal Address; Locations
Nice to have
• The colour blue, clouds on the background

```html
<!DOCTYPE html>
<html lang="en">
<head>
<meta charset="utf-8">
<title>Meridale Holdings Australia – Business Card</title>
<link href="https://fonts.googleapis.com/css2?family=Open+Sans:wght@400;600;700&display=swap" rel="stylesheet">
<style>
  :root{
    --page-bg:#e9ecef;
    --card-light:#f3f4f6;
    --blue-mid:#3176b5;
    --blue-deep:#0e63ab;
    --blue-dark:#0455a3;
    --cloud:#85cae6;
    --white:#ffffff;
  }
  *{box-sizing:border-box;margin:0;padding:0}
  html,body{width:1200px;height:900px;overflow:hidden}
  body{
    background:var(--page-bg);
    font-family:"Open Sans",Arial,sans-serif;
    display:flex;align-items:center;justify-content:center;
  }
  .business-card{
    position:relative;width:1000px;height:610px;overflow:hidden;
    box-shadow:0 10px 30px rgba(0,0,0,.18);
    color:var(--white);
  }
  .sky-backdrop{
    position:absolute;inset:0;
    background:
      radial-gradient(ellipse 220px 110px at 640px 300px, rgba(206,233,245,.35), transparent 70%),
      radial-gradient(ellipse 260px 120px at 760px 470px, rgba(206,233,245,.3), transparent 70%),
      radial-gradient(ellipse 200px 90px at 880px 60px, rgba(206,233,245,.3), transparent 70%),
      linear-gradient(90deg, var(--card-light) 0%, var(--card-light) 14%, #8fb3d6 34%, var(--blue-mid) 46%, var(--blue-deep) 70%, var(--blue-dark) 100%);
  }
  .brand-mark{
    position:absolute;left:60px;top:250px;
    display:flex;align-items:center;gap:16px;
    color:var(--blue-dark);font-weight:700;font-size:46px;
  }
  .brand-mark .dot{width:34px;height:34px;border-radius:50%;background:var(--blue-dark)}
  .company-name{
    position:absolute;right:42px;top:48px;
    font-size:96px;font-weight:400;letter-spacing:-1px;line-height:1;
  }
  .person{position:absolute;right:42px;top:212px;text-align:right}
  .person-name{font-size:33px;font-weight:700;line-height:1.15}
  .person-role{font-size:26px;font-weight:400}
  .contact-list{position:absolute;right:42px;top:340px;list-style:none;text-align:right}
  .contact-list li{
    display:flex;justify-content:flex-end;align-items:center;gap:16px;
    font-size:25px;line-height:36px;
  }
  .contact-list svg{width:20px;height:20px;fill:var(--white)}
  .locations{
    position:absolute;right:42px;bottom:50px;
    font-size:29px;font-weight:400;word-spacing:2px;
  }
</style>
</head>
<body>
  <div class="business-card">
    <div class="sky-backdrop" role="img" aria-label="Soft blue sky with clouds"></div>

    <div class="brand-mark"><span class="dot"></span>Meridale</div>

    <h1 class="company-name">Meridale</h1>

    <div class="person">
      <p class="person-name">Daniel Hartley</p>
      <p class="person-role">Managing Director</p>
    </div>

    <ul class="contact-list">
      <li>0198 765 432
        <svg viewBox="0 0 20 20"><path d="M6 1h8a1 1 0 0 1 1 1v16a1 1 0 0 1-1 1H6a1 1 0 0 1-1-1V2a1 1 0 0 1 1-1zm1 2v12h6V3zm3 13a1 1 0 1 0 0 2 1 1 0 0 0 0-2z"/></svg>
      </li>
      <li>044-198 765 432
        <svg viewBox="0 0 20 20"><path d="M4 1l4 1 1 4-2 2a11 11 0 0 0 5 5l2-2 4 1 1 4-2 2C9 19 1 11 2 3z"/></svg>
      </li>
      <li>info@meridalemail.com
        <svg viewBox="0 0 20 20"><path d="M2 4h16v12H2zm1.5 1.5L10 11l6.5-5.5z"/></svg>
      </li>
      <li>www.meridaleonline.com
        <svg viewBox="0 0 20 20"><circle cx="10" cy="10" r="8.5"/><path d="M6 6c2 0 3 1 3 3s-2 2-2 4M13 4c-1 2 0 3 2 4" stroke="#0e63ab" stroke-width="1.6" fill="none"/></svg>
      </li>
    </ul>

    <p class="locations">Sydney | Melbourne | Brisbane | Singapore</p>
  </div>
</body>
</html>
```